contemporary upscale hair salon

we need a business card design for a modern upscale salon. I would like the card to be vertical, simple, and easy to read. I would like a black matte finish on the info side with white on the back of the card, white lettering with a splash of red incorporated somewhere in there. I also want to incorporate embossing and/or cut out in the letters. The info I would like; Name of the business (Vessa Salon) stylist name (Joan) phone number(5093146620) and web address (www.vessasalon-example.com) I am open to putting shears on the card but without it looking too cheap. Looking for something really modern and edgy. these are just ideas I have, but feel free to show me your creative ideas.
please note: the website is still under construction please do not use any images or colors off the web page. Also i currently do not have a logo, that will be a future project.

```html
<!DOCTYPE html>
<html lang="en">
<head>
<meta charset="utf-8">
<title>Vessa Salon – Business Card</title>
<link rel="stylesheet" href="https://fonts.googleapis.com/css2?family=Open+Sans:wght@400&display=swap">
<style>
  :root {
    --stage: #e6e4e1;
    --card-black: #000000;
    --wave-dark-top: #3a3a3a;
    --wave-dark-bottom: #1c1c1c;
    --card-white: #ffffff;
    --wave-grey: #c4c5c7;
    --ink-white: #ffffff;
    --ink-dark: #1a1a1a;
    --ink-grey: #6d6e70;
    --accent-red: #be1e2d;
    --font-text: "Open Sans", Arial, sans-serif;
  }
  html, body {
    margin: 0;
    padding: 0;
    width: 1200px;
    height: 1005px;
    overflow: hidden;
    background: var(--stage);
    font-family: var(--font-text);
  }
  .stage {
    position: relative;
    width: 1200px;
    height: 1005px;
  }
  .card {
    position: absolute;
    top: 187px;
    width: 410px;
    height: 630px;
    border-radius: 14px;
    overflow: hidden;
    box-shadow: 0 6px 18px rgba(0,0,0,0.25);
  }
  .card-wave {
    position: absolute;
    inset: 0;
    width: 100%;
    height: 100%;
  }
  /* Back side */
  .card-back { left: 150px; background: var(--card-black); }
  .card-back .brand-name {
    position: absolute;
    top: 215px;
    left: 0;
    width: 100%;
    text-align: center;
    color: var(--ink-white);
    font-size: 46px;
    letter-spacing: 1px;
  }
  .card-back .brand-dot {
    position: absolute;
    left: 182px;
    top: 440px;
    width: 46px;
    height: 46px;
    border-radius: 50%;
    background: var(--accent-red);
  }
  /* Info side */
  .card-front { left: 640px; background: var(--card-white); }
  .card-front .brand-name {
    position: absolute;
    top: 74px;
    left: 50px;
    color: var(--ink-dark);
    font-size: 22px;
    letter-spacing: 0.5px;
  }
  .card-front .brand-dot {
    position: absolute;
    top: 70px;
    right: 56px;
    width: 36px;
    height: 36px;
    border-radius: 50%;
    background: var(--accent-red);
  }
  .stylist-name {
    position: absolute;
    top: 200px;
    right: 56px;
    color: var(--accent-red);
    font-size: 32px;
    margin: 0;
  }
  .stylist-role {
    position: absolute;
    top: 263px;
    right: 50px;
    color: var(--ink-grey);
    font-size: 19px;
    letter-spacing: 12px;
    margin: 0;
  }
  .contact {
    position: absolute;
    left: 50px;
    bottom: 36px;
    color: var(--ink-dark);
    font-size: 14px;
    line-height: 24px;
  }
  .contact .web { font-size: 15px; letter-spacing: 3.6px; }
</style>
</head>
<body>
<main class="stage">
  <section class="card card-back" aria-label="Card back">
    <svg class="card-wave" viewBox="0 0 410 630" preserveAspectRatio="none" aria-hidden="true">
      <defs>
        <linearGradient id="darkWave" x1="0" y1="0" x2="0" y2="1">
          <stop offset="0" stop-color="var(--wave-dark-top)"/>
          <stop offset="1" stop-color="var(--wave-dark-bottom)"/>
        </linearGradient>
      </defs>
      <path d="M0,460 C60,560 150,600 240,585 C320,570 325,430 355,375 C375,340 395,328 410,322 L410,630 L0,630 Z" fill="url(#darkWave)"/>
    </svg>
    <div class="brand-name">Vessa Salon</div>
    <div class="brand-dot" aria-hidden="true"></div>
  </section>

  <section class="card card-front" aria-label="Card info side">
    <svg class="card-wave" viewBox="0 0 410 630" preserveAspectRatio="none" aria-hidden="true">
      <path d="M0,300 C80,325 130,370 150,420 C180,495 240,525 300,522 C370,518 400,450 410,390 L410,630 L0,630 Z" fill="var(--wave-grey)"/>
    </svg>
    <div class="brand-name">Vessa Salon</div>
    <div class="brand-dot" aria-hidden="true"></div>
    <h1 class="stylist-name">Joan</h1>
    <p class="stylist-role">stylist</p>
    <div class="contact">
      <div class="phone">T: 509 314 6620</div>
      <div class="web">www.vessasalon-example.com</div>
    </div>
  </section>
</main>
</body>
</html>
```